Flyer für Installationsfirma für hochwertige Multimedia- und Beschallungslösungen, insbesonder in Kirchen und öffentlichen Bereichen mit Menschenansammlungen
Zielgruppe
Wir sind eine Installationsfirma für hochwertige Multimedia- und Beschallungslösungen in akustisch schwierigen Räumen. Im weiteren auch der Umbau auf LED Leuchten und dazugehörende Steuerungen. Unser Geschäft ist in Festinstallationen und Rentalbereich 'unterteilt' Weitere Infos auch auf www. alpen-ton.ch
Unser Zielpublikum sind die Festinstallation für Kirchen und öffentliche Räume. Mehrzweckräume, Bühnen, Kirchen, Aulas, Bahnhofshallen, Warteräume, Konferenzräume, Tagungszentren usw. Bei diesem Flyer sollen speziell die Kirchen beworben werden. Es ist wichtig dass nebst den oben beschriebenen Leistungen auch die Displaylösung für Liedanzeigen hervorgehoben wird.
Aufgabenstellung
Ansprechender Werbe-Flyer A4 2 Seitig
Spezifische Bilder und Texte zu den versch. Angebotsbereichen für Kirchen im Anhang. Vorschläge des Grafikers sind willkommen !
Die Texte und Bilder sollten von uns angepasst und korrigiert werden können !

```html
<!DOCTYPE html>
<html lang="de">
<head>
<meta charset="utf-8">
<title>Alpenton Flyer – Audio &amp; Visual für Kirchen</title>
<link rel="stylesheet" href="https://fonts.googleapis.com/css2?family=Poppins:wght@500;600;700&family=Open+Sans:wght@400;600;700&display=swap">
<style>
  :root{
    --bg:#e9e7e8;
    --navy:#1b2232;
    --navy-deep:#151b28;
    --footer:#1f3a57;
    --blue:#2a9fd8;
    --white:#ffffff;
    --text-soft:#c9ced8;
    --pink:#c3307e;
    --violet:#5a2a63;
    --wood:#8a6a45;
    --stone:#b9ab92;
  }
  *{box-sizing:border-box;margin:0;padding:0}
  html,body{width:1200px;height:800px;overflow:hidden;background:var(--bg)}
  body{font-family:"Open Sans",sans-serif;color:var(--white);position:relative}

  .page{position:absolute;top:117px;width:400px;height:566px;background:var(--navy);overflow:hidden;
    box-shadow:0 10px 24px rgba(0,0,0,.18)}
  .page--front{left:180px}
  .page--back{left:620px}

  /* front */
  .hero-photo{position:absolute;left:0;top:0;width:400px;height:250px;
    background:linear-gradient(180deg,#8e2f5a 0%,var(--pink) 28%,#a54a90 52%,var(--violet) 75%,var(--navy) 100%)}
  .brand-corner{position:absolute;top:26px;right:22px;display:flex;align-items:center;gap:6px;
    font-family:"Poppins",sans-serif;font-weight:600;font-size:12px;letter-spacing:.08em;color:var(--white)}
  .brand-corner .dot{width:10px;height:10px;border-radius:50%;background:var(--white)}
  .headline{position:absolute;top:252px;left:0;width:400px;text-align:center;
    font-family:"Poppins",sans-serif;font-weight:700;font-size:24px;line-height:1.15;letter-spacing:-.01em}
  .accent{color:var(--blue)}
  .intro{position:absolute;top:328px;left:30px;width:340px;text-align:center;font-size:7.6px;line-height:1.6;color:var(--text-soft)}
  .features{position:absolute;top:398px;left:22px;width:356px;display:flex;justify-content:space-between}
  .feature{width:86px;text-align:center;font-family:"Poppins",sans-serif;font-weight:500;font-size:11px;line-height:1.3}
  .feature svg{display:block;margin:0 auto 10px;width:42px;height:42px}

  .footer{position:absolute;left:0;bottom:0;width:400px;height:52px;background:var(--footer);
    display:flex;align-items:center;padding:0 22px;gap:18px}
  .footer-brand{font-family:"Poppins",sans-serif;font-weight:500;font-size:18px;letter-spacing:.06em}
  .footer-contact{font-size:7.6px;font-weight:700;line-height:1.7}

  /* back */
  .services-title{position:absolute;top:26px;left:0;width:400px;text-align:center;
    font-family:"Poppins",sans-serif;font-weight:700;font-size:25px;letter-spacing:-.01em;
    text-shadow:0 0 22px rgba(42,159,216,.35)}
  .service{position:absolute;left:28px;width:344px;height:72px;display:flex;gap:14px;align-items:flex-start}
  .service--reverse{flex-direction:row-reverse}
  .service-photo{flex:0 0 110px;height:70px;border:2px solid var(--white);
    background:linear-gradient(100deg,#4a3a2a 0%,var(--wood) 40%,var(--stone) 70%,#9b8c72 100%)}
  .service-body{flex:1}
  .service-title{font-family:"Poppins",sans-serif;font-weight:600;font-size:12.5px;margin-bottom:4px;text-transform:uppercase}
  .service-text{font-size:7.4px;line-height:1.6;color:var(--text-soft)}
  .cta{position:absolute;top:450px;left:55px;width:290px;height:44px;border:1.5px solid var(--blue);
    display:flex;align-items:center;justify-content:center;text-align:center;
    font-weight:600;font-size:8.6px;line-height:1.5;letter-spacing:.02em}
  .page--back .footer{bottom:0}
</style>
</head>
<body>

<section class="page page--front">
  <div class="hero-photo" role="img" aria-label="Barocker Kircheninnenraum mit Altar, in Pink und Violett beleuchtet"></div>
  <div class="brand-corner"><span class="dot"></span>ALPENTON</div>

  <h1 class="headline">BENÖTIGEN SIE <span class="accent">AUDIO &amp;</span><br><span class="accent">VISUAL</span> FÜR IHRE KIRCHE?</h1>

  <p class="intro">Mit passenden, effizient eingesetzten Mitteln sorgen wir für Aufmerksamkeit bei Ihren Besucherinnen und Besuchern. Sie müssen sich um nichts kümmern. Anhand Ihrer Ideen und Budgetvorgaben entwickeln wir die optimalen Lösungen für Ihre Installation und liefern Ihnen den kompetenten Rundum-Service aus einer Hand.</p>

  <div class="features">
    <div class="feature">
      <svg viewBox="0 0 42 42" fill="none" stroke="#fff" stroke-width="1.6"><circle cx="21" cy="18" r="14"/><circle cx="21" cy="18" r="10"/><path d="M14 30l-3 9 6-3 3 4 1-8M28 30l3 9-6-3-3 4"/></svg>
      25 Jahre<br>Erfahrung
    </div>
    <div class="feature">
      <svg viewBox="0 0 42 42" fill="none" stroke="#fff" stroke-width="1.6"><circle cx="21" cy="18" r="14"/><polygon points="21,10 23.4,15.5 29,16 24.7,19.6 26,25 21,22 16,25 17.3,19.6 13,16 18.6,15.5"/></svg>
      Hochwertige<br>Ausrüstung
    </div>
    <div class="feature">
      <svg viewBox="0 0 42 42" fill="none" stroke="#fff" stroke-width="1.6"><path d="M21 24c-6-4-9-7-9-11a4.5 4.5 0 0 1 9-1 4.5 4.5 0 0 1 9 1c0 4-3 7-9 11z"/><path d="M8 34h26"/></svg>
      Umfassender<br>Service
    </div>
    <div class="feature">
      <svg viewBox="0 0 42 42" fill="none" stroke="#fff" stroke-width="1.6"><circle cx="13" cy="16" r="4"/><circle cx="21" cy="12" r="5"/><circle cx="29" cy="16" r="4"/><path d="M6 34v-6a7 7 0 0 1 14 0v6M14 34v-8a7 7 0 0 1 14 0v8M22 34v-6a7 7 0 0 1 14 0v6"/></svg>
      engagiertes<br>Team
    </div>
  </div>

  <footer class="footer">
    <span class="footer-brand">ALPENTON</span>
    <span class="footer-contact">Bergstrasse 12 | 6430 Schwyz | 041 555 12 34<br>mail@alpen-ton.ch | www.alpen-ton.ch</span>
  </footer>
</section>

<section class="page page--back">
  <h2 class="services-title">UNSERE <span class="accent">LEISTUNGEN</span></h2>

  <article class="service" style="top:80px">
    <div class="service-photo" role="img" aria-label="Lautsprecher an einer Kirchensäule neben dem Altar mit Blumen"></div>
    <div class="service-body">
      <h3 class="service-title accent">Audio</h3>
      <p class="service-text">Lorem ipsum dolor sit amet, consectetuer adipiscing elit, sed diam nonummy nibh euismod tincidunt ut laoreet dolore magna aliquam erat volutpat. Ut wisi enim ad minim veniam, quis nostrud exerci tation.</p>
    </div>
  </article>

  <article class="service service--reverse" style="top:172px">
    <div class="service-photo" role="img" aria-label="LED-Beleuchtung im Altarraum einer Kirche"></div>
    <div class="service-body">
      <h3 class="service-title"><span class="accent">LED</span> Beleuchtung</h3>
      <p class="service-text">Lorem ipsum dolor sit amet, consectetuer adipiscing elit, sed diam nonummy nibh euismod tincidunt ut laoreet dolore magna aliquam erat volutpat. Ut wisi enim ad minim veniam, quis nostrud exerci tation.</p>
    </div>
  </article>

  <article class="service" style="top:264px">
    <div class="service-photo" role="img" aria-label="Steuerungstechnik in einer Kirche"></div>
    <div class="service-body">
      <h3 class="service-title"><span class="accent">Intergration</span>/Steuerung</h3>
      <p class="service-text">Lorem ipsum dolor sit amet, consectetuer adipiscing elit, sed diam nonummy nibh euismod tincidunt ut laoreet dolore magna aliquam erat volutpat. Ut wisi enim ad minim veniam, quis nostrud exerci tation.</p>
    </div>
  </article>

  <article class="service service--reverse" style="top:356px">
    <div class="service-photo" role="img" aria-label="Liedanzeige-Display im Kirchenraum"></div>
    <div class="service-body">
      <h3 class="service-title"><span class="accent">Lieder</span>/Textanzeigen</h3>
      <p class="service-text">Lorem ipsum dolor sit amet, consectetuer adipiscing elit, sed diam nonummy nibh euismod tincidunt ut laoreet dolore magna aliquam erat volutpat. Ut wisi enim ad minim veniam, quis nostrud exerci tation.</p>
    </div>
  </article>

  <div class="cta">KONTAKTIEREN SIE UNS UNVERBINDLICH FÜR EIN<br>PERSÖNLICHES BERATUNGSGESPRÄCH.</div>

  <footer class="footer">
    <span class="footer-brand">ALPENTON</span>
    <span class="footer-contact">Bergstrasse 12 | 6430 Schwyz | 041 555 12 34<br>mail@alpen-ton.ch | www.alpen-ton.ch</span>
  </footer>
</section>

</body>
</html>
```